web page layout, style , color, font & flow design

We are developing a single page application. The SPA (single page application) will display natural gas pipeline flow data once the customer logs on. The customer has a choice of the region, the pipeline, the zone on the pipeline, whether the point is a delivery point or receipt point and the state the pipeline flows through.
we have jumpstarted the project and are attaching a pdf of the same.

we are using mockingbird for the wireframe. any designer is free to use this tool to make changes.

A mockingbird wireframe link is added below. you are free to use it and to make changes. please save the changed wireframe in a different name

we are looking for inputs on layout, style , color, font & flow.

A logo jpg file has also been attached.

Target Market(s)

this single web page is going to be used by natural gas traders and schedulers day in and day out. the application is more of business to business corporate application.

Industry/Entity Type

Delivery

Requirements
Must have
• layout ,flow, size, color, font , ease of use.

```html
<!DOCTYPE html>
<html lang="en">
<head>
<meta charset="utf-8">
<title>Wholesale NG Supply Analysis</title>
<link rel="stylesheet" href="https://fonts.googleapis.com/css2?family=Arimo:wght@400;700&display=swap">
<style>
:root{
  --page-bg:#0088c8;
  --header-bg:#000000;
  --panel-bg:#49c9fa;
  --tabs-bg:#00a4e4;
  --tab-line:#1296d2;
  --tab-text:#0b6594;
  --tab-active-text:#ffffff;
  --title:#f8c800;
  --select-bg:#00b5f5;
  --select-arrow-bg:#0a8ac2;
  --select-arrow:#055a84;
  --select-text:#0d4766;
  --button-bg:#0a84c4;
  --th-bg:#0a8ccb;
  --row-a:#80d9fc;
  --row-b:#b8ebfd;
  --grid:#5ccaf2;
  --ink:#0b1b24;
  --white:#ffffff;
}
*{box-sizing:border-box;margin:0;padding:0}
html,body{width:1200px;height:808px;overflow:hidden}
body{position:relative;background:var(--page-bg);font-family:"Arimo",Arial,sans-serif;color:var(--ink)}

.header-band{position:absolute;left:0;top:0;width:902px;height:448px;background:var(--header-bg)}
.brand{position:absolute;left:24px;top:16px;display:flex;align-items:center;gap:12px}
.brand-mark{width:74px;height:74px;background:var(--white)}
.brand-name{font-size:18px;color:var(--white)}
.app-title{position:absolute;left:396px;top:38px;width:430px;text-align:center;font-size:27px;font-weight:400;color:var(--title);white-space:nowrap}

.panel{position:absolute;left:22px;top:113px;width:1158px;height:630px;background:var(--panel-bg)}
.region-tabs{display:flex;height:70px;background:var(--tabs-bg)}
.region-tab{display:flex;align-items:center;justify-content:center;font-size:19px;color:var(--tab-text);border-right:1px solid var(--tab-line);white-space:nowrap}
.region-tab:last-child{border-right:none}
.region-tab.is-active{background:var(--panel-bg);color:var(--tab-active-text)}

.filter{position:absolute;height:41px;background:var(--select-bg);font-size:15px;display:flex;align-items:center;padding-left:15px;white-space:nowrap}
.filter .label{color:var(--select-text)}
.filter.pipeline .label{color:var(--white)}
.filter .arrow{position:absolute;right:6px;top:7px;width:28px;height:27px;background:var(--select-arrow-bg)}
.filter .arrow svg{display:block;margin:10px auto 0}

.submit-btn{position:absolute;left:783px;top:178px;width:121px;height:43px;background:var(--button-bg);color:var(--white);font-size:18px;display:flex;align-items:center;justify-content:center}

.flow-table{position:absolute;left:26px;top:274px;width:1106px;border-collapse:collapse;table-layout:fixed;font-size:18px}
.flow-table th{height:48px;background:var(--th-bg);color:var(--white);font-weight:400;text-align:left;padding-left:13px;border-right:1px solid var(--grid);white-space:nowrap}
.flow-table td{height:43px;padding-left:13px;border-right:1px solid var(--grid);border-bottom:1px solid var(--grid);white-space:nowrap;overflow:hidden}
.flow-table th:last-child,.flow-table td:last-child{border-right:none}
.flow-table tbody tr:nth-child(odd){background:var(--row-a)}
.flow-table tbody tr:nth-child(even){background:var(--row-b)}
</style>
</head>
<body>
<div class="header-band"></div>
<div class="brand">
  <div class="brand-mark"></div>
  <span class="brand-name">Crestfield</span>
</div>
<h1 class="app-title">Wholesale NG Supply Analysis</h1>

<main class="panel">
  <nav class="region-tabs">
    <div class="region-tab is-active" style="width:205px">NORTH EAST</div>
    <div class="region-tab" style="width:182px">MID WEST</div>
    <div class="region-tab" style="width:197px">SOUTH EAST</div>
    <div class="region-tab" style="width:209px">SOUTH WEST</div>
    <div class="region-tab" style="width:185px">CENTRAL</div>
    <div class="region-tab" style="width:180px">WEST</div>
  </nav>

  <div class="filter" style="left:28px;top:121px;width:233px"><span class="label">Location Type</span><span class="arrow"><svg width="14" height="8"><path d="M0 0h14L7 8z" fill="var(--select-arrow)"/></svg></span></div>
  <div class="filter" style="left:279px;top:121px;width:230px"><span class="label">States</span><span class="arrow"><svg width="14" height="8"><path d="M0 0h14L7 8z" fill="var(--select-arrow)"/></svg></span></div>
  <div class="filter" style="left:530px;top:121px;width:227px"><span class="label">Zones</span><span class="arrow"><svg width="14" height="8"><path d="M0 0h14L7 8z" fill="var(--select-arrow)"/></svg></span></div>
  <div class="filter pipeline" style="left:783px;top:120px;width:319px"><span class="label">Harborline</span><span class="arrow"><svg width="14" height="8"><path d="M0 0h14L7 8z" fill="var(--select-arrow)"/></svg></span></div>

  <div class="filter" style="left:28px;top:180px;width:233px"><span class="label">Gas Day</span><span class="arrow"><svg width="14" height="8"><path d="M0 0h14L7 8z" fill="var(--select-arrow)"/></svg></span></div>
  <div class="filter" style="left:279px;top:180px;width:230px"><span class="label">Cycle</span><span class="arrow"><svg width="14" height="8"><path d="M0 0h14L7 8z" fill="var(--select-arrow)"/></svg></span></div>
  <div class="filter" style="left:530px;top:180px;width:227px"><span class="label">Posting Time</span><span class="arrow"><svg width="14" height="8"><path d="M0 0h14L7 8z" fill="var(--select-arrow)"/></svg></span></div>
  <div class="submit-btn">SUBMIT</div>

  <table class="flow-table">
    <colgroup>
      <col style="width:125px"><col style="width:135px"><col style="width:134px"><col style="width:133px">
      <col style="width:150px"><col style="width:141px"><col style="width:141px"><col style="width:147px">
    </colgroup>
    <thead>
      <tr><th>Gas Day</th><th>Location</th><th>Loc_Name</th><th>Flow_Ind</th><th>Loc_Desc</th><th>Op_Cap</th><th>Sch_Cap</th><th>Op_avail_cap</th></tr>
    </thead>
    <tbody>
      <tr><td>10/14/24</td><td>00410</td><td>Ridge Pt</td><td>R</td><td>Receipt</td><td>250,000</td><td>231,400</td><td>18,600</td></tr>
      <tr><td>10/14/24</td><td>00527</td><td>Bay Gate</td><td>D</td><td>Delivery</td><td>180,000</td><td>172,250</td><td>7,750</td></tr>
      <tr><td>10/14/24</td><td>00633</td><td>Elm Hill</td><td>R</td><td>Interconnect</td><td>320,000</td><td>298,100</td><td>21,900</td></tr>
      <tr><td>10/14/24</td><td>00748</td><td>Pine Ford</td><td>D</td><td>City Gate</td><td>95,000</td><td>88,420</td><td>6,580</td></tr>
      <tr><td>10/14/24</td><td>00852</td><td>Stone Rd</td><td>D</td><td>Delivery</td><td>140,000</td><td>139,000</td><td>1,000</td></tr>
      <tr><td>10/14/24</td><td>00961</td><td>Cedar Lk</td><td>R</td><td>Storage</td><td>210,000</td><td>164,300</td><td>45,700</td></tr>
    </tbody>
  </table>
</main>
</body>
</html>
```